Clear Plastic Card Design

I am looking to have a business card designed from my logo icon. I am looking to match the style of a different business card I have attached in the files.
Looking for a card that is plastic, with layers of transparency in the shape of my logo icon (also attached in the files) - not a circle like the other card. The winning design will incorporate the red icon logo on the front and back and include the charity's name, "Lanterns for the Weary" in the same or similar font, as well as an email and phone number. For now, use the email: email@lanternsfortheweary.org and the phone number 555-318-4072.
We like how the sample business card has transparency, partial and full opacity layers and a matching color scheme. Files will need to be in vector so that our business card printing company can work with it.
UPDATE:
We've some excellent designs in, thank you everyone! I got an early review from the owner, and he requested a minor redirect to find his perfect design. He wants the design to stand out by NOT being a rectangle. Try instead a circle, square, or best yet - something that falls in the outline of the logo icon, either fully or partially. Thank you, everyone!
Contact Information for Business Card
Lanterns for the Weary text should be incorporated as well as a phone and email.
Look and feel

```html
<!DOCTYPE html>
<html lang="en">
<head>
<meta charset="utf-8">
<title>Lanterns for the Weary – Clear Round Card</title>
<link rel="stylesheet" href="https://fonts.googleapis.com/css2?family=Open+Sans:ital,wght@0,600;0,800;1,600&display=swap">
<style>
  :root {
    --page-bg: #e6dcd8;
    --page-glow: #f3ece9;
    --card-clear: rgba(255, 255, 255, 0.42);
    --card-frost: rgba(255, 255, 255, 0.38);
    --card-edge: rgba(255, 255, 255, 0.85);
    --brand-red: #c3101c;
    --brand-mark: rgba(226, 52, 24, 0.88);
    --ink: #3a3a3a;
  }
  * { margin: 0; padding: 0; box-sizing: border-box; }
  html, body {
    width: 1200px;
    height: 900px;
    overflow: hidden;
    font-family: "Open Sans", Arial, sans-serif;
  }
  .canvas {
    position: relative;
    width: 1200px;
    height: 900px;
    background: radial-gradient(circle at 50% 45%, var(--page-glow) 0%, var(--page-bg) 70%);
  }
  .round-card {
    position: absolute;
    left: 396px;
    top: 229px;
    width: 404px;
    height: 404px;
    border-radius: 50%;
    background: var(--card-clear);
    border: 1.5px solid var(--card-edge);
    box-shadow: 0 8px 26px rgba(120, 80, 70, 0.10), inset 0 0 22px rgba(255, 255, 255, 0.55);
  }
  .round-card__frost {
    position: absolute;
    left: 22px;
    top: 22px;
    width: 360px;
    height: 360px;
    border-radius: 50%;
    background: var(--card-frost);
  }
  .brand-mark {
    position: absolute;
    left: 127px;
    top: 46px;
    width: 150px;
    height: 150px;
    border-radius: 50%;
    background: var(--brand-mark);
  }
  .charity-name {
    position: absolute;
    left: 0;
    width: 404px;
    top: 218px;
    text-align: center;
    font-weight: 800;
    font-size: 33px;
    line-height: 38px;
    color: var(--brand-red);
    text-transform: uppercase;
    letter-spacing: -0.3px;
  }
  .contact-email {
    position: absolute;
    left: 0;
    width: 404px;
    top: 302px;
    text-align: center;
    font-style: italic;
    font-weight: 600;
    font-size: 15.5px;
    line-height: 22px;
    color: var(--ink);
    letter-spacing: 0.3px;
  }
  .contact-phone {
    position: absolute;
    left: 0;
    width: 404px;
    top: 334px;
    height: 34px;
    display: flex;
    justify-content: center;
    align-items: center;
    gap: 6px;
    font-weight: 600;
    font-size: 25px;
    color: var(--ink);
  }
  .contact-phone__icon {
    width: 29px;
    height: 29px;
    flex: none;
  }
</style>
</head>
<body>
  <main class="canvas">
    <section class="round-card">
      <div class="round-card__frost"></div>
      <div class="brand-mark" aria-hidden="true"></div>
      <h1 class="charity-name">Lanterns for<br>the Weary</h1>
      <p class="contact-email">email@lanternsfortheweary.org</p>
      <p class="contact-phone">
        <svg class="contact-phone__icon" viewBox="0 0 30 30" aria-hidden="true">
          <circle cx="15" cy="15" r="14.5" fill="#d3121c"/>
          <path d="M10.2 8.6c.5-.4 1.2-.3 1.5.2l1.6 2.4c.3.5.2 1.1-.2 1.4l-1 .8c.7 1.7 2.1 3.2 3.8 4.1l.9-1c.4-.4 1-.5 1.4-.2l2.4 1.5c.5.3.6 1 .3 1.5l-.9 1.3c-.5.7-1.4 1-2.2.8-4.1-1.1-7.3-4.3-8.4-8.4-.2-.8.1-1.7.8-2.2z" fill="#fff"/>
          <path d="M16.5 9.2a5 5 0 0 1 4.3 4.3M16.7 6.6a7.6 7.6 0 0 1 6.7 6.7" stroke="#fff" stroke-width="1.3" fill="none" stroke-linecap="round"/>
        </svg>
        555-318-4072
      </p>
    </section>
  </main>
</body>
</html>
```